Dental Office Business Card

We need a business card for our pediatric dentistry office.
On one side the design needs to contain the following:
our logo (attached)
Vento Pediatric Grins
Soraya Kadbelani, DDS
Board Certified Pediatric Dentist
Tel: (555) 318-2747)
Fax: (555) 264-8031
Email: info@ventopediatricgrins.example
Web: www.ventopediatricgrins.example
Address: 41 Brindle Ave, Suite 208, Wellesley, MA 02099

On the other side of the card, the design needs to have an appointment reminder (date and time as well as day of the week) similar to the design attached (no need for appointment reason “For”)

```html
<!DOCTYPE html>
<html lang="en">
<head>
<meta charset="utf-8">
<title>Vento Pediatric Grins – Business Card</title>
<link rel="stylesheet" href="https://fonts.googleapis.com/css2?family=Montserrat:wght@400;600;700&family=EB+Garamond:wght@400;500&display=swap">
<style>
  :root {
    --page-bg: #e3e5e3;
    --card-white: #f1f1f1;
    --brand-green: #92c49a;
    --brand-green-deep: #86b98e;
    --ink: #1b1b1b;
  }
  * { box-sizing: border-box; margin: 0; padding: 0; }
  html, body { width: 1200px; height: 1200px; overflow: hidden; }
  body { background: var(--page-bg); position: relative; font-family: "Montserrat", sans-serif; color: var(--ink); }

  .card { position: absolute; top: 250px; width: 400px; height: 700px; border-radius: 4px; overflow: hidden; }
  .card-front { left: 160px; background: linear-gradient(180deg, var(--brand-green) 0%, var(--brand-green-deep) 100%); }
  .card-back { left: 640px; background: var(--card-white); }

  .front-top { position: absolute; left: 0; top: 0; width: 100%; height: 175px; background: var(--card-white); }
  .brand-mark { position: absolute; left: 0; top: 0; width: 100%; height: 175px; display: flex; align-items: center; justify-content: center; gap: 12px; }
  .brand-dot { width: 22px; height: 22px; border-radius: 50%; background: var(--brand-green); }
  .brand-name { font-weight: 600; font-size: 24px; color: var(--ink); }

  .front-details { position: absolute; left: 0; top: 352px; width: 100%; text-align: center; }
  .doctor-name { font-weight: 700; font-size: 24px; letter-spacing: 0.2px; }
  .doctor-title { font-size: 16.5px; margin-top: 6px; }
  .contact-icons { display: flex; justify-content: center; gap: 11px; margin-top: 26px; }
  .contact-icons svg { width: 16px; height: 16px; }
  .contact-list { list-style: none; margin-top: 12px; font-size: 17px; line-height: 25.5px; }
  .divider { width: 94px; height: 1.5px; background: var(--ink); margin: 14px auto 16px; }
  .address { font-style: normal; font-size: 17px; line-height: 25px; }

  .back-content { position: absolute; left: 0; top: 700px; width: 700px; height: 400px; transform-origin: 0 0; transform: rotate(-90deg); font-family: "EB Garamond", serif; }
  .heading-main { position: absolute; left: 172px; top: 50px; font-size: 33px; letter-spacing: 17.5px; font-weight: 400; }
  .heading-sub { position: absolute; left: 228px; top: 108px; display: flex; align-items: center; gap: 8px; font-size: 36px; }
  .heading-sub svg { width: 34px; height: 30px; }
  .field { position: absolute; display: flex; align-items: flex-end; font-size: 21px; letter-spacing: 3px; }
  .field-line { border-bottom: 1.2px solid var(--ink); margin-left: 6px; height: 1px; }
  .field-for { left: 99px; top: 178px; }
  .field-date { left: 99px; top: 220px; }
  .weekdays { position: absolute; left: 99px; top: 274px; display: flex; gap: 10px; font-size: 14px; list-style: none; }
  .weekdays li { display: flex; align-items: center; gap: 8px; }
  .checkbox { width: 14px; height: 14px; border: 1.2px solid var(--ink); display: inline-block; }
  .field-time { left: 99px; top: 312px; }
  .meridiem { position: absolute; left: 398px; top: 318px; font-size: 14px; word-spacing: 8px; }
</style>
</head>
<body>
  <section class="card card-front" aria-label="Card front">
    <div class="front-top"></div>
    <div class="brand-mark">
      <span class="brand-dot"></span>
      <span class="brand-name">Vento Pediatric Grins</span>
    </div>
    <div class="front-details">
      <h1 class="doctor-name">Soraya Kadbelani, DDS</h1>
      <p class="doctor-title">Board Certified Pediatric Dentist</p>
      <div class="contact-icons" aria-hidden="true">
        <svg viewBox="0 0 24 24"><path fill="#1b1b1b" d="M6.6 10.8c1.4 2.8 3.8 5.1 6.6 6.6l2.2-2.2c.3-.3.7-.4 1-.2 1.1.4 2.3.6 3.6.6.6 0 1 .4 1 1V20c0 .6-.4 1-1 1C10.6 21 3 13.4 3 4c0-.6.4-1 1-1h3.5c.6 0 1 .4 1 1 0 1.3.2 2.5.6 3.6.1.3 0 .7-.2 1z"/></svg>
        <svg viewBox="0 0 24 24"><path fill="#1b1b1b" d="M6 2h12v5H6zM3 8h18c1 0 2 1 2 2v7h-4v5H5v-5H1v-7c0-1 1-2 2-2zm4 8v4h10v-4z"/></svg>
        <svg viewBox="0 0 24 24"><path fill="#1b1b1b" d="M2 5h20v14H2zm2 2v.5l8 5 8-5V7l-8 5z"/></svg>
        <svg viewBox="0 0 24 24"><circle cx="12" cy="12" r="9" fill="none" stroke="#1b1b1b" stroke-width="2.2"/><path d="M3 12h18M12 3c3 3 3 15 0 18M12 3c-3 3-3 15 0 18" fill="none" stroke="#1b1b1b" stroke-width="1.8"/></svg>
      </div>
      <ul class="contact-list">
        <li>(555) 318-2747)</li>
        <li>(555) 264-8031</li>
        <li>info@ventopediatricgrins.example</li>
        <li>www.ventopediatricgrins.example</li>
      </ul>
      <div class="divider"></div>
      <address class="address">41 Brindle Ave, Suite 208,<br>Wellesley, MA 02099</address>
    </div>
  </section>

  <section class="card card-back" aria-label="Card back, appointment reminder">
    <div class="back-content">
      <h2 class="heading-main">APPOINTMENT</h2>
      <div class="heading-sub">
        <svg viewBox="0 0 34 30" aria-hidden="true"><path d="M16 3 5 15l11 12M28 3 17 15l11 12" fill="none" stroke="#1b1b1b" stroke-width="3.2"/></svg>
        <span>Reminder</span>
        <svg viewBox="0 0 34 30" aria-hidden="true"><path d="M6 3l11 12L6 27M18 3l11 12-11 12" fill="none" stroke="#1b1b1b" stroke-width="3.2"/></svg>
      </div>
      <div class="field field-for"><span>FOR:</span><span class="field-line" style="width:436px"></span></div>
      <div class="field field-date"><span>DATE:</span><span class="field-line" style="width:412px"></span></div>
      <ul class="weekdays">
        <li><span class="checkbox"></span>Mon</li>
        <li><span class="checkbox"></span>Tue</li>
        <li><span class="checkbox"></span>Wed</li>
        <li><span class="checkbox"></span>Thu</li>
        <li><span class="checkbox"></span>Fri</li>
        <li><span class="checkbox"></span>Sun</li>
        <li><span class="checkbox"></span>Sat</li>
        <li><span class="checkbox"></span></li>
      </ul>
      <div class="field field-time"><span>TIME:</span><span class="field-line" style="width:200px"></span></div>
      <span class="meridiem">a.m. p.m.</span>
    </div>
  </section>
</body>
</html>
```